Quarrow financial services, is a financial company that provides consultancy, brokerage services, and funding.

we will be providing the clients with insights, knowledge and data with regards to the financial markets.

with the brokerage services we will try to find the suitable counterparts that provide them with the best investments that suits their needs and expected return.

Target Market(s)

financial institutions, Corporates, high-net worth individuals

Industry/Entity Type

Financial Service

Contact Information for Business Card

Font styles to use
Other font styles liked:
• applemyungjo

Colors
00a990
848484

Requirements
Must have
• the logo at the back
Nice to have
• Finesse
Should not have
• boldness

```html
<!DOCTYPE html>
<html lang="en">
<head>
<meta charset="utf-8">
<title>Quarrow Financial Services — Business Card</title>
<link href="https://fonts.googleapis.com/css2?family=Cinzel:wght@400&family=Noto+Serif:wght@400;600&family=Roboto:wght@400&display=swap" rel="stylesheet">
<style>
  :root {
    --page: #eeeeee;
    --card: #ffffff;
    --ink: #39444a;
    --text: #555555;
    --teal-band: #3f9c89;
    --teal-name: #2e8b78;
    --sage: #c9d6bf;
    --band-edge: #6a6a6a;
  }
  * { box-sizing: border-box; margin: 0; padding: 0; }
  html, body { width: 1200px; height: 443px; overflow: hidden; }
  body { background: var(--page); position: relative; font-family: "Noto Serif", serif; }

  .card {
    position: absolute;
    top: 72px;
    background: var(--card);
    border-radius: 14px;
    overflow: hidden;
  }
  .card--front { left: 82px; width: 484px; height: 294px; }
  .card--back  { left: 602px; width: 481px; height: 292px; }

  .brand-name {
    font-family: "Cinzel", serif; font-weight: 400; color: var(--ink);
    letter-spacing: 0.04em; line-height: 1; white-space: nowrap;
  }
  .brand-sub {
    font-family: "Cinzel", serif; font-weight: 400; color: var(--ink);
    letter-spacing: 0.18em; line-height: 1; white-space: nowrap;
  }
  .tagline {
    font-family: "Cinzel", serif; font-weight: 400;
    letter-spacing: 0.08em; line-height: 1; white-space: nowrap;
  }

  /* Front */
  .front-brand__square {
    position: absolute; left: 207px; top: 66px;
    width: 70px; height: 70px; background: var(--sage);
  }
  .front-brand__text {
    position: absolute; left: 0; right: 0; top: 174px;
    display: flex; flex-direction: column; align-items: center;
  }
  .front-brand__text .brand-name { font-size: 38px; }
  .front-brand__text .brand-sub { font-size: 11.5px; margin-top: 7px; }
  .front-brand__text .tagline { font-size: 9.5px; color: var(--ink); margin-top: 6px; }

  /* Back */
  .back-brand__square {
    position: absolute; left: 28px; top: 24px;
    width: 40px; height: 76px; background: var(--sage);
  }
  .back-brand__text {
    position: absolute; left: 86px; top: 40px;
    display: flex; flex-direction: column; align-items: center;
  }
  .back-brand__text .brand-name { font-size: 29px; }
  .back-brand__text .brand-sub { font-size: 9px; margin-top: 5px; }

  .person { position: absolute; left: 30px; top: 136px; }
  .person__name {
    font-family: "Noto Serif", serif; font-weight: 600; font-size: 20px;
    color: var(--teal-name); line-height: 1.1;
  }
  .person__role {
    font-family: "Roboto", sans-serif; font-size: 12px; color: var(--text); margin-top: 6px;
  }

  .contacts { position: absolute; left: 32px; top: 193px; list-style: none; }
  .contacts li {
    display: flex; align-items: center; gap: 10px; height: 17.5px;
    font-size: 12.5px; color: var(--text);
  }
  .contacts svg { width: 11px; height: 11px; fill: var(--teal-band); flex: none; }
  .address {
    position: absolute; left: 30px; top: 250px;
    font-size: 13px; color: var(--text);
  }

  .side-band {
    position: absolute; top: 0; right: 0; width: 46px; height: 100%;
    background: var(--teal-band); border-left: 5px solid var(--band-edge);
  }
  .side-band .tagline {
    position: absolute; left: 50%; top: 50%;
    transform: translate(-50%, -50%) rotate(-90deg);
    color: #ffffff; font-size: 8.5px;
  }
</style>
</head>
<body>

  <section class="card card--front" aria-label="Card front">
    <span class="front-brand__square" aria-hidden="true"></span>
    <div class="front-brand__text">
      <div class="brand-name">QUARROW</div>
      <div class="brand-sub">FINANCIAL SERVICES</div>
      <div class="tagline">CLEAR INSIGHT FOR EVERY INVESTMENT</div>
    </div>
  </section>

  <section class="card card--back" aria-label="Card back">
    <span class="back-brand__square" aria-hidden="true"></span>
    <div class="back-brand__text">
      <div class="brand-name">QUARROW</div>
      <div class="brand-sub">FINANCIAL SERVICES</div>
    </div>

    <div class="person">
      <div class="person__name">Elias Marlow</div>
      <div class="person__role">Managing Director</div>
    </div>

    <ul class="contacts">
      <li>
        <svg viewBox="0 0 12 12" aria-hidden="true"><path d="M1 4c0-2 2-3 5-3s5 1 5 3v1H8.5V3.8H3.5V5H1z M2.5 6h7l1 5h-9z"/></svg>
        00-310-475-9182
      </li>
      <li>
        <svg viewBox="0 0 12 12" aria-hidden="true"><path d="M6 0.5a5.5 5.5 0 1 0 0 11a5.5 5.5 0 1 0 0-11zM6 1.6c.6.6 1.2 1.9 1.3 3.6H4.7C4.8 3.5 5.4 2.2 6 1.6zM4.7 6.8h2.6C7.2 8.5 6.6 9.8 6 10.4 5.4 9.8 4.8 8.5 4.7 6.8zM1.7 5.2c.2-1.5 1.2-2.7 2.5-3.3-.5.9-.8 2-.9 3.3zm0 1.6h1.6c.1 1.3.4 2.4.9 3.3C2.9 9.5 1.9 8.3 1.7 6.8zm6.1 3.3c.5-.9.8-2 .9-3.3h1.6c-.2 1.5-1.2 2.7-2.5 3.3zm.9-4.9c-.1-1.3-.4-2.4-.9-3.3 1.3.6 2.3 1.8 2.5 3.3z"/></svg>
        www.quarrowfinance.com
      </li>
      <li>
        <svg viewBox="0 0 12 12" aria-hidden="true"><path d="M0.5 2h11v8h-11z M1.5 3l4.5 3.6L10.5 3v-.1h-9z" fill-rule="evenodd"/></svg>
        elias@quarrowfinance.com
      </li>
    </ul>

    <div class="address">2614 Linden Crest Road Fairhaven California 90417</div>

    <div class="side-band">
      <div class="tagline">CLEAR INSIGHT FOR EVERY INVESTMENT</div>
    </div>
  </section>

</body>
</html>
```